Re-Design Business Card and Logo for Plastic Printing

Business is a small financial planning (investments, insurance, retirement, etc.) firm. The majority of our clients are 55+ years old, professional occupations (pilots, doctors, bankers, etc.) but not necessarily "high net worth."
I would like to have a design that would be used on clear plastic business cards. I have found a vendor that makes these but I do not have the ability to design these like I want.
I do have one proof but I just don't feel like it's the right one for me. Also, I feel that I need some help with a logo redesign so maybe someone could handle that for me as well.
I want the final design to "eye catching" but still be tasteful. I am open to suggestion regarding colors and such.
I will include the old design as well as the new proof I have to give you an idea of what I current have. Keep in mind, I have no allegiance to the attached designs.
For the second file (Business Card New Proof), the white space shown will be transparent when printed on plastic card.
Target Market(s)
Mostly people age 55+ in professional occupations.
Industry/Entity Type
Financial Service
Contact Information for Business Card
Looking for design that can be printed on clear plastic cards (if possible).
Logo Text
KLT - Kestrel Lakeview Trust
Requirements
Must have
- Must be double sided because disclosure is required for compliance reasons.
Designations (must include the Registered trademark symbol as follows)...
MBA, ChFC®, CLU®, CRPS®
Nice to have
- The little icons next to email, phone and fax are nice.
Should not have
- I think I would like to eliminate the Owner and Co-Founder line that you see on the attachments.

```html
<!DOCTYPE html>
<html lang="en">
<head>
<meta charset="utf-8">
<title>Kestrel Lakeview Trust – Business Card</title>
<link rel="stylesheet" href="https://fonts.googleapis.com/css2?family=Josefin+Sans:wght@300;400;600&display=swap">
<style>
  :root {
    --page-bg: #dfe3ea;
    --clear-area: #f3f5f8;
    --navy-light: #34497a;
    --navy-dark: #18244d;
    --navy-stripe: #1f2e5c;
    --band-grey: #3c3d42;
    --line-white: #ffffff;
    --ink-navy: #2b3b66;
    --text-light: #e9edf5;
    --icon-grey: #c9ced9;
    --icon-ink: #1c2a55;
  }
  * { box-sizing: border-box; margin: 0; padding: 0; }
  html, body { width: 806px; height: 1200px; overflow: hidden; }
  body {
    background: var(--page-bg);
    font-family: "Josefin Sans", sans-serif;
    position: relative;
  }
  .card {
    position: absolute;
    left: 188px;
    width: 503px;
    height: 287px;
    border-radius: 28px;
    overflow: hidden;
    background: var(--clear-area);
    box-shadow: 0 4px 14px rgba(20, 30, 60, 0.25);
  }
  .card--front { top: 137px; }
  .card--back { top: 736px; }
  .card__swoosh { position: absolute; inset: 0; width: 503px; height: 287px; }

  .brand {
    position: absolute;
    display: flex;
    align-items: center;
    gap: 10px;
    color: var(--ink-navy);
    font-weight: 600;
    font-size: 22px;
    line-height: 1.05;
  }
  .brand__dot {
    width: 26px; height: 26px;
    border-radius: 50%;
    background: var(--ink-navy);
    flex: none;
  }
  .card--front .brand { left: 18px; top: 116px; width: 235px; }

  .contact {
    position: absolute;
    right: 18px;
    text-align: right;
    color: var(--text-light);
    font-weight: 300;
    white-space: nowrap;
  }
  .contact__name { top: 41px; font-size: 20px; font-weight: 400; letter-spacing: 1px; color: #fff; }
  .contact__creds { top: 65px; font-size: 13px; letter-spacing: 0.5px; }
  .contact__address { top: 118px; font-size: 12.5px; line-height: 17px; letter-spacing: 0.5px; }
  .contact__lines { top: 194px; font-size: 12.5px; line-height: 17px; letter-spacing: 0.4px; }
  .contact__line { display: flex; justify-content: flex-end; align-items: center; gap: 6px; }
  .contact__icon { width: 12px; height: 12px; flex: none; }

  .card--back .brand {
    left: 17px; top: 18px; width: 190px;
    flex-direction: column; align-items: flex-start; gap: 26px;
    color: #fff; font-size: 20px;
  }
  .card--back .brand__dot { background: #fff; width: 46px; height: 46px; margin-left: 43px; }
  .disclosure {
    position: absolute;
    left: 17px; top: 160px; width: 188px;
    color: var(--text-light);
    font-size: 10.3px;
    font-weight: 300;
    line-height: 13.4px;
  }
</style>
</head>
<body>

<section class="card card--front" aria-label="Card front">
  <svg class="card__swoosh" viewBox="0 0 503 287" aria-hidden="true">
    <defs>
      <linearGradient id="navyFront" x1="0" y1="0" x2="1" y2="1">
        <stop offset="0" stop-color="#34497a"/>
        <stop offset="1" stop-color="#18244d"/>
      </linearGradient>
    </defs>
    <path d="M236,0 C312,70 302,200 188,287 L503,287 L503,0 Z" fill="var(--band-grey)"/>
    <path d="M250,0 C324,70 314,200 204,287 L503,287 L503,0 Z" fill="var(--navy-stripe)" stroke="var(--line-white)" stroke-width="1.2"/>
    <path d="M262,0 C336,70 326,200 218,287 L503,287 L503,0 Z" fill="url(#navyFront)" stroke="var(--line-white)" stroke-width="1.2"/>
  </svg>

  <div class="brand"><span class="brand__dot"></span><span>Kestrel Lakeview Trust</span></div>

  <div class="contact contact__name">MARCUS HOLLEN</div>
  <div class="contact contact__creds">MBA, ChFC®, CLU®, CRPS®</div>
  <div class="contact contact__address">1180 Harbor View Dr,<br>Suite 210<br>Seabrook Point, VA 23190</div>
  <div class="contact contact__lines">
    <div class="contact__line">(555) 301-4826
      <svg class="contact__icon" viewBox="0 0 12 12"><circle cx="6" cy="6" r="6" fill="var(--icon-grey)"/><path d="M3,4.5 Q6,2.5 9,4.5 L8.5,5.5 L7.5,5 L7.5,4.5 Q6,4 4.5,4.5 L4.5,5 L3.5,5.5 Z M4,6.5 h4 v2 h-4 Z" fill="var(--icon-ink)"/></svg>
    </div>
    <div class="contact__line">(555) 720-1948 Toll Free
      <svg class="contact__icon" viewBox="0 0 12 12"><circle cx="6" cy="6" r="6" fill="var(--icon-grey)"/><rect x="4" y="2.8" width="4" height="6.4" rx="0.8" fill="none" stroke="var(--icon-ink)" stroke-width="1"/></svg>
    </div>
    <div class="contact__line">mhollen@kestrellakeview.com
      <svg class="contact__icon" viewBox="0 0 12 12"><circle cx="6" cy="6" r="6" fill="var(--icon-grey)"/><rect x="3" y="4" width="6" height="4.2" fill="none" stroke="var(--icon-ink)" stroke-width="0.9"/><path d="M3,4 L6,6.4 L9,4" fill="none" stroke="var(--icon-ink)" stroke-width="0.9"/></svg>
    </div>
  </div>
</section>

<section class="card card--back" aria-label="Card back">
  <svg class="card__swoosh" viewBox="0 0 503 287" aria-hidden="true">
    <defs>
      <linearGradient id="navyBack" x1="0" y1="0" x2="1" y2="1">
        <stop offset="0" stop-color="#34497a"/>
        <stop offset="1" stop-color="#18244d"/>
      </linearGradient>
    </defs>
    <path d="M266,0 C232,70 228,200 316,287 L0,287 L0,0 Z" fill="var(--band-grey)"/>
    <path d="M248,0 C216,70 212,200 292,287 L0,287 L0,0 Z" fill="var(--navy-stripe)" stroke="var(--line-white)" stroke-width="1.2"/>
    <path d="M236,0 C204,70 200,200 280,287 L0,287 L0,0 Z" fill="url(#navyBack)" stroke="var(--line-white)" stroke-width="1.2"/>
  </svg>

  <div class="brand"><span class="brand__dot"></span><span>Kestrel Lakeview Trust</span></div>

  <p class="disclosure">Marcus Hollen is a registered representative of and offers securities and advisory services through Northgate Capital Securities Corporation, Member SIFA. Northgate Capital Securities Corporation is a member of the Northgate Capital Group which is the marketing name for Northgate National Corporation and its affiliates.</p>
</section>

</body>
</html>
```